KTR Business Holiday Card 2019

5 x 7 front and back HOLIDAY CARD for our business - see attachments for wording and elements we'd like to include. Also an attachment of sample designs we like.

Target Market(s)

Our current and prospective clients

Colors
f04a50
85abd2
abd037
33a6d7

Requirements
Must have
• I have included an attachment where I drafted the elements we need in the card. I have also included an attachment with a few sample cards that we like the look of as a guide.

```html
<!DOCTYPE html>
<html lang="en">
<head>
<meta charset="utf-8">
<title>KTR Holiday Card 2019</title>
<link rel="stylesheet" href="https://fonts.googleapis.com/css2?family=Cinzel:wght@400&family=Great+Vibes&family=Barlow+Semi+Condensed:wght@400;600&display=swap">
<style>
  :root{
    --page:#c9cacc;
    --navy:#0f2f6f;
    --navy-deep:#0a2558;
    --red:#d3243a;
    --white:#ffffff;
    --ink:#1f2430;
    --sky:#33a6d7;
    --ice:#85abd2;
    --band:#e3eef8;
  }
  *{margin:0;padding:0;box-sizing:border-box}
  html,body{width:1200px;height:794px;overflow:hidden}
  body{background:var(--page);position:relative;font-family:"Barlow Semi Condensed",sans-serif}

  .card{position:absolute;top:216px;width:487px;height:347px;overflow:hidden}
  .card--front{left:99px;background:radial-gradient(ellipse at 50% 45%,var(--navy) 0%,var(--navy-deep) 100%)}
  .card--back{left:630px;background:var(--white)}

  .front__eyebrow{position:absolute;left:209px;top:28px;font-family:"Cinzel",serif;font-size:13px;letter-spacing:.5px;color:var(--white);white-space:nowrap}
  .front__frame{position:absolute;left:65px;top:49px;width:358px;height:242px;background:var(--red);padding:6px}
  .front__photo{width:100%;height:100%;background:linear-gradient(180deg,#4a5048 0%,#6b3a3a 38%,#b2323a 62%,#8b2a30 100%)}
  .front__greeting{position:absolute;left:67px;top:290px;font-family:"Great Vibes",cursive;font-size:31px;color:var(--white);white-space:nowrap}

  .flake{position:absolute;border-radius:50%}
  .flake--light{background:radial-gradient(circle,rgba(255,255,255,.85) 0%,rgba(255,255,255,.15) 70%,transparent 100%)}
  .flake--blue{background:radial-gradient(circle,var(--sky) 0%,rgba(51,166,215,.35) 65%,transparent 100%)}

  .back__message{position:absolute;left:28px;top:60px;font-family:"Great Vibes",cursive;font-size:21px;line-height:29px;color:var(--ink)}
  .back__signature{position:absolute;right:55px;top:175px;font-family:"Great Vibes",cursive;font-size:22px;color:var(--ink);white-space:nowrap}

  .back__band{position:absolute;left:0;right:0;top:222px;height:12px;background:linear-gradient(180deg,var(--white),var(--band))}
  .back__footer{position:absolute;left:0;right:0;top:234px;height:91px;background:var(--white)}
  .back__base{position:absolute;left:0;right:0;top:325px;height:22px;background:linear-gradient(180deg,var(--band),var(--white))}

  .brand{position:absolute;left:36px;top:32px;display:flex;align-items:center;gap:6px}
  .brand__dot{width:10px;height:10px;border-radius:50%;background:var(--red)}
  .brand__name{font-weight:600;font-size:22px;letter-spacing:1px;color:var(--sky)}
  .partners__rule{position:absolute;left:150px;top:14px;width:2px;height:66px;background:var(--red)}
  .partners{position:absolute;left:156px;top:10px;list-style:none;font-size:7px;line-height:8.8px;color:var(--ink);white-space:nowrap}
  .partners b{font-weight:600;color:var(--sky)}
</style>
</head>
<body>
  <section class="card card--front">
    <span class="flake flake--light" role="img" aria-label="snowflake ornament" style="left:38px;top:20px;width:62px;height:62px"></span>
    <span class="flake flake--light" role="img" aria-label="snowflake ornament" style="left:165px;top:14px;width:26px;height:26px"></span>
    <span class="flake flake--light" role="img" aria-label="snowflake ornament" style="left:12px;top:93px;width:38px;height:38px"></span>
    <span class="flake flake--light" role="img" aria-label="snowflake ornament" style="left:40px;top:172px;width:30px;height:30px"></span>
    <span class="flake flake--light" role="img" aria-label="snowflake ornament" style="left:405px;top:265px;width:62px;height:62px"></span>
    <p class="front__eyebrow">From our family to yours...</p>
    <div class="front__frame">
      <div class="front__photo" role="img" aria-label="Family photo of five people seated on red steps before a red door"></div>
    </div>
    <p class="front__greeting">Happy Holidays &amp; Thank You</p>
  </section>

  <section class="card card--back">
    <span class="flake flake--blue" role="img" aria-label="snowflake ornament" style="left:376px;top:30px;width:54px;height:54px"></span>
    <span class="flake flake--blue" role="img" aria-label="snowflake ornament" style="left:418px;top:72px;width:36px;height:36px"></span>
    <span class="flake flake--blue" role="img" aria-label="snowflake ornament" style="left:406px;top:128px;width:18px;height:18px"></span>
    <p class="back__message">In the spirit of the season, we extend a heartfelt<br>thank you for your business this year.<br>May you have a wonderful holiday season and<br>a Happy new year.</p>
    <p class="back__signature">Daniel and Joanne Keller</p>

    <div class="back__band"></div>
    <div class="back__footer">
      <div class="brand"><span class="brand__dot"></span><span class="brand__name">KTR</span></div>
      <div class="partners__rule"></div>
      <ul class="partners">
        <li><b>Brayton Medical:</b> ARVEN balloon dilation catheter, DURAL laser resistant ET tube, TRAVIO tracheostomy tubes</li>
        <li><b>Keystone Surgical:</b> biphasic nerve stimulator/locator</li>
        <li><b>Harbor Medical:</b> OCR Implants, Myringotomy Tubes, ENT instruments</li>
        <li><b>Auralis:</b> Fenwick ear dressing, Marlow irrigation suction tubing</li>
        <li><b>Lumora LLC:</b> Flexible and rigid scopes</li>
        <li><b>Vantor Optics USA:</b> OR Microscopes</li>
        <li><b>Verida ENT:</b> Biologic autologous tissue</li>
        <li><b>Calder Medical USA:</b> Precision electrosurgery bipolars and monopolars</li>
      </ul>
    </div>
    <div class="back__base"></div>
  </section>
</body>
</html>
```